Velora Lounge Duo Flyer - info and save 20%

We need a flyer designed around the look of our website - that retro feel - it can give some brief info on our duo and we need to present an offer of 20% off our normal prices for live music at private or corporate events and weddings.
Two hours $590 Now $472
Three hours $690 Now $ 552
Four hours $790 Now $632
Five hours $890 Now $712
About our duo:
Velora Duo - Live Jazz and Cocktail Music
Set the atmosphere with classy cocktail music and jazz at your next event of distinction. Marnie Holt on Piano and Gavin Thorley on the Bass - professional and dedicated musicians. All venues and all occasions. Servicing Brisbane & South-East Queensland. Acoustic or Electric - all venue sizes.
Testimonials:
Sat. March 21, 2013 | Fendrix Awards Dinner at the Palmvale Arts Centre
The Velora Duo provided the perfect entertainment for our Awards Dinner. It was fantastic to have the combination of purely background music and more upbeat music with vocals. Marnie was brilliant to deal with from the initial booking stage to the event and ensured that the entertainment option provided was the most suitable for our event.
Dana Whitcombe, Fendrix Pty Ltd
_______________________________________________________________________
Sat. June 26, 2012 | Wedding at the Riverbend Hall of Qld
We had Velora Duo play at our Cocktail Wedding Reception for the first couple of hours and they were simply delightful! The music was diverse, fun and great way to create a buzzing atmosphere while still having your guests being able to enjoy their conversations. As everyone knows weddings can be stressful but it was such a pleasure was dealing with Marnie Holt (pianist) of Velora Duo as she was completely helpful and professional in organising the music list and the arrangement and put our minds at rest knowing we were dealing with such professional and experienced musicians. It was a wonderful start to the evening and we had many complements on the wonderful music from our guests! It again completely reaffirmed to us how important good music is for creating a memorable experience on your wedding day and we cannot recommend Velora Duo and their pianist Marnie Holt enough!
Tessa & Martin, June 2012,
Fri. April 21st, 2011 | Surprise Birthday Party – Kestrel Club
You simply made the evening with your music. Thank you Velora Duo for another great night!”
Doyle Family 2011,
Fri. October 1st, 2010 - ongoing | Harbourview Manor, Queensland
It has been an absolute pleasure to have Marnie & Gavin perform for us at Harbourview Manor. Their love and passion for music is brought to life through their flawless performances and never cease to amaze myself or our guests with what they will come up with next. Marnie and Gavin are such wonderful characters who are willing to go above and beyond to support Harbourview Manor with whatever musical requests and repertoire we require.
Marnie has also been a fantastic help to me with the recommendation of other Brisbane based musicians whose professionalism and commitment to the music industry is faultless.
I would like to thank Marnie and Gavin and the Tidewave Sound team for their continuing musical support to Harbourview Manor.
Colleen Ashby - Assistant House Manager - Harbourview Manor Queensland
Updates
This project was meant to finish today - 25 Aug - I am not sure why it is saying that it has 7 more days to run - but we need it by tomorrow really !! (26 Aug)
This is a message from the printers re the design specs!
Design files> PDF settings. All CMYK colour settings no RGB.
Print ready files to have the noted minimum 3mm bleed design and the noted crop marks for final trim size.
1 up front, 1 up backs for cards or leaflets etc.

```html
<!DOCTYPE html>
<html lang="en">
<head>
<meta charset="utf-8">
<title>Velora Duo – Tri-fold Brochure</title>
<link rel="stylesheet" href="https://fonts.googleapis.com/css2?family=Bebas+Neue&family=Courier+Prime&family=Raleway:wght@300;500&display=swap">
<style>
  :root {
    --backdrop: #d9d9d9;
    --charcoal: #4a4849;
    --charcoal-mid: #535152;
    --teal: #7aa9ae;
    --cream: #f1e4c8;
    --rust: #d7694b;
    --ink: #4f4d4e;
    --heading: "Bebas Neue", "Oswald", sans-serif;
    --body: "Courier Prime", "Courier New", monospace;
    --display: "Raleway", "Helvetica Neue", sans-serif;
  }
  * { box-sizing: border-box; margin: 0; padding: 0; }
  html, body {
    width: 1200px; height: 838px; overflow: hidden;
    background: var(--backdrop);
  }
  .brochure {
    position: absolute; left: 60px; top: 39px;
    width: 1080px; height: 760px;
    display: flex;
    overflow: hidden;
    box-shadow: 0 10px 30px rgba(0,0,0,.25);
  }
  .panel { width: 360px; height: 760px; position: relative; overflow: hidden; }

  /* shared */
  .hatch {
    height: 8px;
    background: repeating-linear-gradient(60deg, var(--rust) 0 2px, transparent 2px 5px);
  }
  .hatch--cream {
    background: repeating-linear-gradient(60deg, var(--cream) 0 2px, transparent 2px 5px);
  }

  /* about panel */
  .panel--about { background: var(--charcoal); padding: 96px 42px 0; color: var(--cream); }
  .about__title { font-family: var(--heading); font-size: 58px; line-height: 1; letter-spacing: 1px; font-weight: 400; }
  .panel--about .hatch { margin: 10px 0 32px; width: 220px; }
  .about__text { font-family: var(--body); font-size: 15px; line-height: 1.45; letter-spacing: .3px; }
  .panel--about .hatch.mid { margin: 52px 0 30px; width: 276px; }
  .about__tagline {
    font-family: var(--heading); font-size: 30px; line-height: 1.1; text-align: center; letter-spacing: .5px;
  }
  .about__tagline span { display: block; white-space: nowrap; }
  .panel--about .hatch.end { margin: 30px 0 0; width: 276px; }

  /* offer panel */
  .panel--offer { background: var(--charcoal-mid); padding: 50px 40px 0; color: var(--cream); text-align: center; }
  .discount {
    width: 96px; height: 96px; border-radius: 50%;
    background: var(--rust); border: 3px solid var(--cream);
    margin: 0 auto 20px; color: var(--cream);
    display: flex; flex-direction: column; justify-content: center;
    font-family: var(--heading); line-height: .9;
  }
  .discount__amount { font-size: 36px; }
  .discount__label { font-size: 18px; }
  .offer__lead { font-family: var(--heading); font-size: 24px; line-height: 1.1; letter-spacing: .5px; }
  .panel--offer .hatch { margin: 20px 0; }
  .prices { list-style: none; font-family: var(--heading); font-size: 24px; line-height: 1.55; }
  .prices li { display: flex; justify-content: center; align-items: center; gap: 8px; }
  .price-tag {
    background: var(--rust); color: var(--cream); padding: 0 6px; font-size: 20px; line-height: 1.2;
  }
  .contact__title { font-family: var(--heading); font-size: 26px; margin-top: 46px; letter-spacing: .5px; }
  .contact__line { font-family: var(--heading); font-size: 21px; margin-top: 14px; letter-spacing: .5px; }
  .web-ribbon {
    display: inline-block; margin-top: 20px; padding: 8px 34px;
    background: var(--rust); color: var(--cream);
    font-family: var(--heading); font-size: 22px; letter-spacing: .5px;
    clip-path: polygon(0 0, 100% 0, 94% 50%, 100% 100%, 0 100%, 6% 50%);
  }

  /* cover panel */
  .panel--cover { background: var(--teal); }
  .cover__masthead { padding: 44px 20px 0; text-align: center; height: 170px; }
  .cover__title {
    font-family: var(--display); font-weight: 300; color: var(--cream);
    font-size: 40px; letter-spacing: 3px; line-height: 1; white-space: nowrap;
  }
  .cover__ribbon {
    display: inline-block; margin-top: 16px; padding: 6px 30px;
    background: var(--cream); color: var(--ink);
    font-family: var(--heading); font-size: 18px; letter-spacing: 1px; white-space: nowrap;
    clip-path: polygon(0 0, 100% 0, 95% 50%, 100% 100%, 0 100%, 5% 50%);
  }
  .cover__photo {
    position: absolute; left: 40px; top: 170px; width: 320px; height: 250px;
    background: linear-gradient(135deg, #5a3422 0%, #9a6a3e 45%, #3d2a20 100%);
  }
  .cover__lineup { position: absolute; left: 30px; top: 470px; width: 180px; color: var(--ink); }
  .lineup__name { font-family: var(--heading); font-size: 30px; line-height: 1; white-space: nowrap; }
  .lineup__role {
    font-family: var(--heading); font-size: 16px; text-align: right;
    border-top: 1.5px solid var(--ink); margin-top: 6px; padding-top: 2px; margin-bottom: 24px;
  }
  .cover__illustration {
    position: absolute; right: 20px; top: 440px; width: 130px; height: 290px;
    background: radial-gradient(ellipse at 50% 70%, var(--cream) 0 55%, transparent 56%);
  }
</style>
</head>
<body>
  <main class="brochure">
    <section class="panel panel--about">
      <h2 class="about__title">About Us</h2>
      <div class="hatch"></div>
      <p class="about__text">Set the atmosphere with classy cocktail music and jazz at your next event of distinction. Marnie Holt on Piano and Gavin Thorley on the Bass - professional and dedicated musicians. All venues and all occasions. Servicing Brisbane &amp; South-East Queensland. Acoustic or Electric - all venue sizes.</p>
      <div class="hatch mid"></div>
      <p class="about__tagline"><span>Perfect live music</span><span>for private &amp; corporate</span><span>events, weddings</span><span>and dinner music</span></p>
      <div class="hatch end"></div>
    </section>

    <section class="panel panel--offer">
      <div class="discount"><span class="discount__amount">20%</span><span class="discount__label">OFF</span></div>
      <p class="offer__lead">For live music at private or<br>corporate events and weddings</p>
      <div class="hatch hatch--cream"></div>
      <ul class="prices">
        <li>Two hours $590 now <span class="price-tag">$472</span></li>
        <li>Three hours $690 now <span class="price-tag">$552</span></li>
        <li>Four hours $790 now <span class="price-tag">$632</span></li>
        <li>Five hours $890 now <span class="price-tag">$712</span></li>
      </ul>
      <div class="hatch hatch--cream"></div>
      <h3 class="contact__title">Contact Us</h3>
      <p class="contact__line">· 0400 555 218 ·</p>
      <p class="contact__line">HELLO@VELORAJAZZDUO.COM</p>
      <span class="web-ribbon">WWW.VELORAJAZZDUO.COM</span>
    </section>

    <section class="panel panel--cover">
      <header class="cover__masthead">
        <h1 class="cover__title">VELORA DUO</h1>
        <span class="cover__ribbon">CLASSIC COCKTAIL MUSIC</span>
      </header>
      <div class="cover__photo" role="img" aria-label="Photo of the duo performing on grand piano and double bass in a wood-panelled room"></div>
      <div class="cover__lineup">
        <p class="lineup__name">Marnie Holt</p>
        <p class="lineup__role">PIANO</p>
        <p class="lineup__name">Gavin Thorley</p>
        <p class="lineup__role">BASS</p>
      </div>
      <div class="cover__illustration" role="img" aria-label="Cream illustration of a double bass combined with piano keys"></div>
    </section>
  </main>
</body>
</html>
```